Activity List

We need a brochure designed for Brackley House, which is a holiday villa in Sri Lanka. The brochure will be sent to travel agents and holiday travellers by email and also be printed and placed at Brackley House. The brochure should be sophisticated yet indicate a sense of adventure.

```html
<!DOCTYPE html>
<html lang="en">
<head>
<meta charset="utf-8">
<title>Brackley House – Activity List</title>
<link rel="stylesheet" href="https://fonts.googleapis.com/css2?family=Source+Sans+3:ital,wght@0,300;0,400;0,600;1,300;1,400&display=swap">
<style>
  :root {
    --backdrop: #b1d3d3;
    --paper: #f1f1ef;
    --paper-shade: #e6e6e3;
    --teal: #1b8a8f;
    --body-grey: #7d7d7d;
    --note-grey: #8e8e8e;
    --gutter: #cfcfcc;
    --leaf-dark: #2f6e1e;
    --leaf-light: #7fbf4a;
    --sky: #c9dde8;
    --hill: #3f6b34;
    --water: #5e9a8a;
  }
  * { margin: 0; padding: 0; box-sizing: border-box; }
  html, body {
    width: 1200px; height: 700px; overflow: hidden;
    background: var(--backdrop);
    font-family: "Source Sans 3", "Helvetica Neue", sans-serif;
  }
  .spread {
    position: absolute; left: 50px; top: 150px;
    width: 1100px; height: 400px;
    display: flex;
    box-shadow: 0 6px 18px rgba(0,0,0,0.18);
  }
  .page {
    position: relative; width: 550px; height: 400px;
    display: flex; background: var(--paper);
  }
  .page--left { background: linear-gradient(90deg, var(--paper) 80%, var(--paper-shade)); }
  .page--right { background: linear-gradient(90deg, var(--paper-shade), var(--paper) 20%); }
  .page--left::after {
    content: ""; position: absolute; right: 0; top: 0; bottom: 0; width: 1px;
    background: var(--gutter);
  }
  .photo { width: 265px; height: 100%; }
  .photo--tea {
    background: linear-gradient(180deg, #3d7a2a 0%, var(--leaf-light) 45%, var(--leaf-dark) 100%);
  }
  .photo--dam {
    background: linear-gradient(180deg, var(--sky) 0%, #dfe9ee 18%, var(--hill) 35%, #4d7a3e 58%, var(--water) 72%, #41713b 100%);
  }
  .text-panel { flex: 1; padding: 68px 40px 0 30px; position: relative; }
  .activity-title {
    color: var(--teal); font-weight: 400; font-size: 23px; line-height: 1.1;
  }
  .activity-time {
    color: var(--teal); font-size: 13px; margin: 2px 0 16px;
  }
  .activity-body {
    color: var(--body-grey); font-style: italic; font-weight: 300;
    font-size: 12.5px; line-height: 1.25; text-align: justify;
  }
  .activity-note {
    color: var(--note-grey); font-style: italic; font-weight: 300;
    font-size: 9.5px; line-height: 1.35; margin-top: 18px;
  }
  .brand {
    position: absolute; left: 0; right: 0; bottom: 46px;
    display: flex; flex-direction: column; align-items: center; gap: 8px;
  }
  .brand-dot { width: 22px; height: 22px; border-radius: 50%; background: var(--teal); }
  .brand-name {
    color: var(--teal); font-size: 13px; font-weight: 400; letter-spacing: 1.5px;
  }
</style>
</head>
<body>
  <main class="spread">
    <section class="page page--left">
      <div class="photo photo--tea" role="img" aria-label="Hands picking fresh tea leaves in a green tea plantation"></div>
      <div class="text-panel">
        <h2 class="activity-title">From Leaf to Cup</h2>
        <p class="activity-time">(20 minute by foot)</p>
        <p class="activity-body">Walk down to the neighbourhood tea factory for a lesson on how Sri Lanka’s most famous export – tea – is processed. Watch how a batch of freshly packed tea leaves is transformed into the familiar brew that is enjoyed by millions around the world.</p>
        <p class="activity-note">(Activity provided free of charge<br>based on availability)</p>
        <div class="brand">
          <span class="brand-dot"></span>
          <span class="brand-name">THE BRACKLEY HOUSE</span>
        </div>
      </div>
    </section>
    <section class="page page--right">
      <div class="text-panel">
        <h2 class="activity-title">The Kotmale Dam</h2>
        <p class="activity-time">(15 minutes)</p>
        <p class="activity-body">The impressive Kotmale Dam built in the 1980s is just a 15-minute drive from Brackley. The Brackley House manager will accompany you to the dam and give you details on its construction. Take in the majesty of this engineering wonder and if the waters are low catch a glimpse of ancient temples that were submerged during its construction. If interested we will then take you to visit the Mahaweli Maha Seya a gigantic stupa built to replace the lost temples.</p>
        <p class="activity-note">($25 for a group up to 4 people using guest’s<br>vehicle, $50 per group in Brackley House vehicle)</p>
      </div>
      <div class="photo photo--dam" role="img" aria-label="Kotmale Dam wall and reservoir below forested hills under a cloudy sky"></div>
    </section>
  </main>
</body>
</html>
```